Web page for Marcus Penrose Chartered Tax Adviser

I need to take the basic web page that I have created and "Brand it" to be compatible with the corporate logo and stationery created for me by other Pixel Guild designers.
I will need a watermark as well as a distinctive home page and then a branded general page for content including a series of Blogs.

Target Market(s)

My practice deals with expatriates including those looking to invest in Australia.

Industry/Entity Type

Crowd

Font styles to use
Other font styles liked:
• Per logo

Requirements
Must have
• Besides the homepage I will need a general page for content, branded in the same style as the letterheads.
Nice to have
• A watermark to go with the blogs and news content.

```html
<!DOCTYPE html>
<html lang="en">
<head>
<meta charset="utf-8">
<title>Marcus Penrose – Chartered Tax Adviser</title>
<link href="https://fonts.googleapis.com/css2?family=Cinzel:wght@400;500&family=Open+Sans:wdth,wght@75,300;75,400&display=swap" rel="stylesheet">
<style>
:root{
  --navy:#2b4a6b;
  --navy-dark:#1f3c5c;
  --ink:#222;
  --muted:#777;
  --line:#d8dde2;
  --foot-top:#3b6a8d;
  --foot-bottom:#244a72;
  --foot-text:#d6e2ec;
  --hero-a:#c9a77c;
  --hero-b:#7d5a36;
}
*{margin:0;padding:0;box-sizing:border-box}
html,body{width:693px;height:1200px;overflow:hidden;background:#fff}
body{position:relative;font-family:"Open Sans",sans-serif;font-stretch:75%;font-weight:300;color:var(--ink)}
a{color:inherit;text-decoration:none}
.abs{position:absolute}

.topbar{left:0;top:0;width:693px;height:19px;border-bottom:1px solid #eee;font-size:7px;color:#aaa}
.topbar .contact{left:29px;top:5px;display:flex;gap:26px}
.topbar .social{right:30px;top:4px;display:flex;gap:2px}
.topbar .social span{width:8px;height:8px;background:#b5c2d0;border-radius:1px}

.header{left:0;top:19px;width:693px;height:63px}
.brand{left:27px;top:14px;display:flex;align-items:center;gap:6px}
.brand .mark{width:26px;height:26px;border-radius:50%;background:var(--navy)}
.brand .name{font-family:"Cinzel",serif;color:var(--navy);font-size:15px;line-height:1}
.brand .name small{display:block;font-size:5.5px;letter-spacing:2px;margin-top:3px}
.nav{right:30px;top:27px;display:flex;gap:20px;font-family:"Cinzel",serif;font-size:8px;color:#333;align-items:center}
.nav .active{color:var(--navy);border-bottom:1px solid var(--navy);padding-bottom:6px;margin-top:6px}
.nav .search{width:7px;height:7px;border:1.2px solid #aaa;border-radius:50%}

.hero{left:0;top:82px;width:693px;height:376px;background:linear-gradient(120deg,var(--hero-a),#b8905f 45%,var(--hero-b));}
.hero-copy{left:0;top:190px;width:693px;text-align:center;color:#fff;font-family:"Cinzel",serif}
.hero-copy h1{font-size:27px;font-weight:400;letter-spacing:.5px}
.hero-copy p{width:490px;margin:12px auto 0;font-size:9.4px;line-height:13px;padding-bottom:10px;border-bottom:1px solid rgba(255,255,255,.6)}
.hero-copy .btn{display:inline-block;margin-top:21px;border:1px solid #fff;padding:7px 13px;font-size:9px}
.arrow{top:246px;width:12px;height:30px}

.welcome{left:0;top:484px;width:693px;text-align:center}
.welcome h2{font-family:"Cinzel",serif;font-weight:400;color:var(--navy);font-size:20px}
.welcome .lead{margin-top:14px;font-size:12px;color:#222;font-weight:400}
.welcome .body{width:520px;margin:6px auto 0;font-size:8.8px;line-height:13px;color:var(--muted)}
.welcome .btn{display:inline-block;margin-top:15px;background:var(--navy);color:#fff;font-size:9.5px;font-weight:400;padding:8px 11px;border:1px solid #1a3350}
.divider{left:27px;top:650px;width:638px;height:1px;background:var(--line)}

.section-title{font-family:"Cinzel",serif;font-weight:400;color:var(--navy);font-size:19px;top:678px}
.news-item{left:27px;width:260px;height:54px}
.date{left:0;top:0;width:50px;height:54px;background:var(--navy);color:#fff;text-align:center}
.date b{display:block;font-weight:300;font-size:15px;padding-top:8px;height:34px}
.date i{display:block;font-style:normal;font-size:8px;background:var(--navy-dark);height:20px;line-height:20px}
.date::after{content:"";position:absolute;right:-6px;top:0;border-left:6px solid var(--navy);border-bottom:6px solid transparent}
.news-text{left:58px;top:1px;width:210px;font-size:7.6px;line-height:10px;color:#666}
.news-text u{display:block;font-size:8.6px;color:var(--navy);font-weight:400;margin-bottom:4px}
.news-text .more{display:block;margin-top:3px;color:var(--navy);font-size:8px}
.more-news{left:85px;top:935px;font-size:9px;color:var(--navy);font-weight:400}

.blog-card{left:368px;width:296px;height:70px;border:1px solid #e3e3e3}
.blog-card .thumb{left:0;top:0;width:88px;height:69px}
.blog-card .text{left:97px;top:6px;width:192px;font-size:6.6px;line-height:9px;color:#666}
.blog-card .text h3{font-size:8.8px;font-weight:400;color:#222;margin-bottom:2px}
.blog-card .text .by{color:#aaa;margin-bottom:2px}
.blog-card .text .more{display:block;margin-top:5px;color:var(--navy);font-size:7px}

.footer{left:0;top:1000px;width:693px;height:200px;background:linear-gradient(var(--foot-top),var(--foot-bottom));color:var(--foot-text)}
.fcol{top:38px;font-size:7.8px;line-height:13px}
.fcol h4{font-weight:300;font-size:11.5px;color:#fff;padding-bottom:4px;border-bottom:1px dotted rgba(255,255,255,.4);margin-bottom:10px;line-height:14px}
.fcol .row{display:flex;align-items:center;gap:5px;margin-bottom:3px}
.ico{width:11px;height:11px;border:1px solid var(--foot-text);border-radius:50%}
.email{margin-top:8px;width:101px;height:15px;background:#d9e3ea;color:#333;font-size:6.4px;padding:4px 5px;line-height:7px}
.subscribe{margin-top:4px;width:101px;height:17px;background:#1e3d5e;color:#fff;text-align:center;font-size:8px;line-height:17px}
.copyright{left:0;width:693px;text-align:center;font-size:7.6px;color:#a9bfd2;border-top:1px solid rgba(0,0,0,.15);padding-top:13px}
</style>
</head>
<body>

<div class="abs topbar">
  <div class="abs contact"><span>☎ (020) 7946 0382</span><span>✉ hello@penroseadvisory.co</span></div>
  <div class="abs social"><span></span><span></span><span></span><span></span></div>
</div>

<header class="abs header">
  <div class="abs brand">
    <span class="mark"></span>
    <div class="name">Marcus Penrose<small>CHARTERED TAX ADVISER</small></div>
  </div>
  <nav class="abs nav">
    <a class="active">HOME</a><a>ABOUT US</a><a>SERVICES</a><a>BLOG</a><a>NEWS</a><a>CONTACT</a><span class="search"></span>
  </nav>
</header>

<section class="abs hero" role="img" aria-label="Photo of a person typing on a laptop at a desk in warm light"></section>
<div class="abs hero-copy">
  <h1>Marcus Penrose</h1>
  <p>Lorem ipsum dolor sit amet consectetur adipisicing elit, sed do eiusmod tempor incididunt ut labore et dolore magna aliqua. Ut enim ad minim veniam, quis nostrud exercitation ullamco laboris nisi ut aliquip ex ea commodo consequat.</p>
  <a class="btn">Know More</a>
</div>
<svg class="abs arrow" style="left:28px" viewBox="0 0 12 30"><path d="M10 1 L2 15 L10 29" fill="none" stroke="#fff" stroke-width="1.3"/></svg>
<svg class="abs arrow" style="left:653px" viewBox="0 0 12 30"><path d="M2 1 L10 15 L2 29" fill="none" stroke="#fff" stroke-width="1.3"/></svg>

<section class="abs welcome">
  <h2>Welcome to Marcus Penrose</h2>
  <p class="lead">Consectetur adipisicing elit, sed do eiusmod tempor incididunt ut labore et dolore magna aliqua.</p>
  <p class="body">Lorem ipsum dolor sit amet Consectetur adipisicing elit, sed do eiusmod tempor incididunt ut labore et dolore magna aliqua. Ut enim ad minim veniam, quis nostrud exercitation ullamco laboris nisi ut aliquip ex ea commodo consequat. Duis aute irure dolor in reprehenderit in voluptate velit esse cillum dolore eu fugiat nulla pariatur. Excepteur sint occaecat cupidatat non proident, sunt in culpa qui officia deserunt mollit anim id est laborum.</p>
  <a class="btn">KNOW MORE</a>
</section>
<div class="abs divider"></div>

<h2 class="abs section-title" style="left:29px">Latest News &amp; Updates</h2>
<h2 class="abs section-title" style="left:367px">Latest Blog</h2>

<article class="abs news-item" style="top:725px">
  <div class="abs date"><b>07</b><i>DEC</i></div>
  <div class="abs news-text"><u>Lorem ipsum dolor sit amet Consectetur adipisicing elit.</u>Sed do eiusmod tempor incididunt ut labore et dolore magna aliqua. Ut enim ad minim veniam, quis nostrud exercitation ullamco<a class="more">Read More</a></div>
</article>
<article class="abs news-item" style="top:796px">
  <div class="abs date"><b>03</b><i>DEC</i></div>
  <div class="abs news-text"><u>Lorem ipsum dolor sit amet Consectetur adipisicing elit.</u>Sed do eiusmod tempor incididunt ut labore et dolore magna aliqua. Ut enim ad minim veniam, quis nostrud exercitation ullamco<a class="more">Read More</a></div>
</article>
<article class="abs news-item" style="top:862px">
  <div class="abs date"><b>01</b><i>DEC</i></div>
  <div class="abs news-text"><u>Lorem ipsum dolor sit amet Consectetur adipisicing elit.</u>Sed do eiusmod tempor incididunt ut labore et dolore magna aliqua. Ut enim ad minim veniam, quis nostrud exercitation ullamco<a class="more">Read More</a></div>
</article>
<a class="abs more-news">MORE NEWS &gt;&gt;</a>

<article class="abs blog-card" style="top:722px">
  <div class="abs thumb" role="img" aria-label="Photo of a laptop and tablet on a white desk" style="background:linear-gradient(135deg,#e9eef3,#b9c6d2)"></div>
  <div class="abs text"><h3>Lorem ipsum dolor sit amet consectetur adipisicing elit</h3><div class="by">Posted By Elena Marwick</div>Ut enim ad minim veniam, quis nostrud exercitation ullamco laboris nisi ut aliquip ex ea commodo consequat enim ad minim veniam,<a class="more">Read More</a></div>
</article>
<article class="abs blog-card" style="top:804px">
  <div class="abs thumb" role="img" aria-label="Photo of two colleagues reviewing work at a laptop" style="background:linear-gradient(135deg,#c9d2dc,#7d8fa3)"></div>
  <div class="abs text"><h3>Lorem ipsum dolor sit amet consectetur adipisicing elit</h3><div class="by">Posted By Elena Marwick</div>Ut enim ad minim veniam, quis nostrud exercitation ullamco laboris nisi ut aliquip ex ea commodo consequat enim ad minim veniam,<a class="more">Read More</a></div>
</article>
<article class="abs blog-card" style="top:886px">
  <div class="abs thumb" role="img" aria-label="Photo of a team meeting table with charts and documents" style="background:linear-gradient(135deg,#8a6a4e,#3e5f86)"></div>
  <div class="abs text"><h3>Lorem ipsum dolor sit amet consectetur adipisicing elit</h3><div class="by">Posted By Elena Marwick</div>Ut enim ad minim veniam, quis nostrud exercitation ullamco laboris nisi ut aliquip ex ea commodo consequat enim ad minim veniam,<a class="more">Read More</a></div>
</article>

<footer class="abs footer">
  <div class="abs fcol" style="left:31px;width:74px"><h4>NAVIGATION</h4>HOME<br>ABOUT<br>SERVICES<br>BLOG<br>CONTACTS</div>
  <div class="abs fcol" style="left:147px;width:73px"><h4>INFORMATION</h4>PRIVACY POLICY<br>TERMS &amp; CONDITIONS<br>FAQ</div>
  <div class="abs fcol" style="left:274px;width:112px;line-height:10px"><h4 style="margin-bottom:12px">NEWSLETTER</h4>Subscribe our newsletter to know our daily updates and offer.<div class="email">ENTER YOUR EMAIL ID</div><div class="subscribe">SUBSCRIBE</div></div>
  <div class="abs fcol" style="left:453px;width:65px"><h4>FOLLOW US</h4>
    <div class="row"><span class="ico"></span>PULSEFEED</div><div class="row"><span class="ico"></span>CIRCLEHUB</div><div class="row"><span class="ico"></span>CAREERLINK</div><div class="row"><span class="ico"></span>STREAMPLUS</div></div>
  <div class="abs fcol" style="left:571px;width:92px"><h4>OUR LOCATION</h4>
    <div class="row" style="align-items:flex-start"><svg width="9" height="12" viewBox="0 0 9 12"><path d="M4.5 0a4.5 4.5 0 0 0-4.5 4.5C0 8 4.5 12 4.5 12S9 8 9 4.5A4.5 4.5 0 0 0 4.5 0z" fill="#d6e2ec"/><circle cx="4.5" cy="4.5" r="1.6" fill="#35638a"/></svg><span style="margin-left:5px">12 FENWICK LANE,<br>ASHBY UK</span></div>
    <div class="row" style="margin-top:14px"><svg width="10" height="10" viewBox="0 0 10 10"><path d="M2 0l2 2.5-1 1.5a6 6 0 0 0 3 3l1.5-1L10 8 8.5 10C4 10 0 6 0 1.5z" fill="#d6e2ec"/></svg>TEL: +020 7946 0382</div>
    <div class="row"><svg width="10" height="9" viewBox="0 0 10 9"><rect x="2" y="0" width="6" height="3" fill="#d6e2ec"/><rect x="0" y="3" width="10" height="5" rx="1" fill="#d6e2ec"/></svg>FAX: +020 7946 0382</div></div>
  <div class="abs copyright" style="top:158px">Copyrights © 2014. All Rights Reserved.</div>
</footer>

</body>
</html>
```